Webdesign für  FAQ-Finder
Webdesign für FAQ-Finder
Zielgruppe
wiego-lumi.de ist ein FAQ-Finder für werdende / frisch gebackene Eltern in einem ansprechenden, effizienten und modernen Design.
Aufgabenstellung
Ein mobile first Designansatz basierenden auf einem cleanen, modernen Interface und Illustrationen im Stile von:
https://pixelkorb.example/shots/20581934-Tervon-a-fund-for-many
Es gibt noch kein Logo und kein CI. Die Farbwelt soll sich an dem Beispiel von
https://www.quarnetpantry.example/collections
orientieren. Gedeckt, warm. Thematisch geht es um Babies.
For structure perhaps like this:
https://pixelkorb.example/shots/20947715-Flexible-layout-for-Sitewerk-theming-service/attachments/7310452?mode=media
https://pixelkorb.example/shots/20633179--Staffing-Role-locator-Query-App
For Content:
https://www.wiegenpfad.example/category/themen/baby/

```html
<!DOCTYPE html>
<html lang="de">
<head>
<meta charset="utf-8">
<title>wiego-lumi.de – Kinderwunsch</title>
<link rel="stylesheet" href="https://fonts.googleapis.com/css2?family=Poppins:wght@400;500;600;700&display=swap">
<style>
  :root {
    --stage-bg: #d4d9e2;
    --screen-bg: #ffffff;
    --ink: #111111;
    --ink-soft: #2a2a2a;
    --accent: #4a3ca6;
    --divider: #e3e3e6;
    --art-lilac: #ebe8fb;
    --art-mint: #d3efe4;
  }
  * { box-sizing: border-box; margin: 0; padding: 0; }
  html, body {
    width: 1066px;
    height: 1200px;
    overflow: hidden;
    background: var(--stage-bg);
    font-family: "Poppins", sans-serif;
    color: var(--ink);
  }
  .screen {
    position: absolute;
    left: 273px;
    top: 20px;
    width: 520px;
    height: 1160px;
    background: var(--screen-bg);
    border-radius: 40px;
    overflow: hidden;
  }
  .site-header {
    position: absolute;
    left: 24px;
    right: 24px;
    top: 66px;
    height: 90px;
  }
  .brand {
    position: absolute;
    left: 0;
    top: 0;
    display: flex;
    flex-direction: column;
    align-items: center;
    gap: 10px;
  }
  .brand-mark {
    width: 60px;
    height: 60px;
    border: 3px solid var(--accent);
    border-radius: 50%;
  }
  .brand-name {
    font-size: 21px;
    font-weight: 500;
    color: var(--ink-soft);
    line-height: 1;
  }
  .menu-toggle {
    position: absolute;
    right: 0;
    top: 40px;
    width: 48px;
    height: 30px;
  }
  .toolbar {
    position: absolute;
    left: 24px;
    right: 24px;
    top: 215px;
    height: 32px;
  }
  .toolbar .back { position: absolute; left: 0; top: 0; }
  .toolbar .search { position: absolute; right: 0; top: 0; }
  .page-title {
    position: absolute;
    left: 24px;
    top: 272px;
    font-size: 40px;
    font-weight: 700;
    line-height: 56px;
    letter-spacing: 0.5px;
  }
  .hero-art {
    position: absolute;
    left: 68px;
    top: 380px;
    width: 384px;
    height: 372px;
    border-radius: 24px;
    background: linear-gradient(180deg, var(--art-lilac) 0%, var(--art-mint) 100%);
  }
  .faq-item {
    position: absolute;
    left: 24px;
    right: 24px;
    top: 806px;
    padding-bottom: 26px;
    border-bottom: 2px solid var(--divider);
  }
  .faq-question {
    font-size: 22px;
    font-weight: 500;
    line-height: 32px;
    padding-right: 70px;
  }
  .faq-toggle {
    position: absolute;
    right: 10px;
    top: 15px;
    width: 22px;
    height: 3px;
    background: var(--accent);
  }
  .faq-answer {
    margin-top: 14px;
    font-size: 19.5px;
    line-height: 32px;
    color: var(--ink-soft);
    padding-right: 64px;
  }
</style>
</head>
<body>
  <main class="screen">
    <header class="site-header">
      <div class="brand">
        <span class="brand-mark"></span>
        <span class="brand-name">wiego-lumi.de</span>
      </div>
      <svg class="menu-toggle" viewBox="0 0 48 30" aria-label="Menü">
        <g stroke="#222" stroke-width="3" stroke-linecap="round">
          <line x1="2" y1="3" x2="46" y2="3"/>
          <line x1="2" y1="15" x2="46" y2="15"/>
          <line x1="2" y1="27" x2="46" y2="27"/>
        </g>
      </svg>
    </header>

    <nav class="toolbar">
      <svg class="back" width="20" height="32" viewBox="0 0 20 32" aria-label="Zurück">
        <polyline points="16,3 4,16 16,29" fill="none" stroke="#222" stroke-width="2.6" stroke-linecap="round" stroke-linejoin="round"/>
      </svg>
      <svg class="search" width="32" height="32" viewBox="0 0 32 32" aria-label="Suche">
        <circle cx="14" cy="14" r="11" fill="none" stroke="#222" stroke-width="2.6"/>
        <line x1="22" y1="22" x2="29" y2="29" stroke="#222" stroke-width="2.6" stroke-linecap="round"/>
      </svg>
    </nav>

    <h1 class="page-title">Kinderwunsch</h1>

    <div class="hero-art" role="img" aria-label="Illustration: Mutter kniet auf einer Wiese vor ihrem Kleinkind, darüber Wolken und ein Vogel"></div>

    <section class="faq-item">
      <h2 class="faq-question">Woran merke ich, dass meinem Baby kalt ist?</h2>
      <span class="faq-toggle"></span>
      <p class="faq-answer">Wenn dein Baby kalte Hände hat, bedeutet das nicht unbedingt, dass dein Baby friert. Fass deinem Baby sanft in den Nacken und fühl, ob dein Kind dort warm ist. Wenn ja, ist alles in Ordnung und dein Baby ist optimal gekleidet.</p>
    </section>
  </main>
</body>
</html>
```